New Software Development Firm Needs Stationery

Brindle Works, LLC is a new software development firm specializing in document management and custom engineering applications. We just completed a logo design project on PixelHarbor.

We also have an open project right now on PixelHarbor for business card design. ** We highly encourage you to submit designs to both projects as we want the two designs to have the same look and feel.

Design must be provided for coordinated letterhead and envelopes that works with the selected business card design on the other project.

We want a clean, professional and modern look that works well with our logo. We also require a recommendation for what PC font to use when printing on the new letterhead and envelopes.

The final submission must include source Photoshop or Illustrator files and any fonts used must be specified exactly.

Target Market(s)

Small to medium business professionals - including manufacturers, civil engineering firms, government agencies, architects, as well as general business.

Industry/Entity Type

Software

Requirements
Must have
• Must work very well with logo and business card design. Must work well with a specified and readily-available font on most PCs.
Nice to have
• White letterhead and envelopes are probably preferred, but we're open to suggestions!

```html
<!DOCTYPE html>
<html lang="en">
<head>
<meta charset="utf-8">
<title>Brindle Works Stationery</title>
<link href="https://fonts.googleapis.com/css2?family=Arimo:wght@400;700&display=swap" rel="stylesheet">
<style>
  :root {
    --backdrop: #b39a7c;
    --paper: #ffffff;
    --ink: #111111;
    --ink-soft: #555555;
    --rule: #222222;
    --accent: #e3111b;
    --card-black: #0c0c0c;
    --box-grey: #d4d4d4;
    --shadow: 0 2px 6px rgba(0,0,0,0.35);
  }
  * { margin: 0; padding: 0; box-sizing: border-box; }
  html, body { width: 1200px; height: 492px; overflow: hidden; }
  body {
    position: relative;
    background: var(--backdrop);
    font-family: "Arimo", Arial, sans-serif;
    color: var(--ink);
  }
  .sheet, .card, .envelope, .flap { position: absolute; }

  /* Letterhead */
  .sheet {
    top: 17px; width: 357px; height: 462px;
    background: var(--paper); box-shadow: var(--shadow);
  }
  .sheet--fax { left: 12px; }
  .sheet--letter { left: 404px; }
  .wordmark { position: absolute; font-weight: 400; letter-spacing: 0.2px; white-space: nowrap; line-height: 1; }
  .sheet .wordmark { left: 26px; top: 36px; font-size: 24px; }
  .sheet-address {
    position: absolute; left: 257px; top: 27px; padding-left: 10px;
    border-left: 1px solid #bbb; font-size: 7.4px; line-height: 8.6px; color: var(--ink-soft);
  }
  .fax-title { position: absolute; left: 25px; top: 84px; font-size: 20px; font-weight: 400; }
  .fax-fields { position: absolute; left: 25px; top: 128px; width: 316px; }
  .fax-row { display: flex; height: 19px; border-bottom: 1px solid var(--rule); align-items: flex-end; font-size: 7px; padding-bottom: 1px; }
  .fax-row span:first-child { width: 163px; }
  .fax-options { position: absolute; left: 25px; top: 205px; display: flex; gap: 15px; font-size: 7px; }
  .fax-options span { display: flex; align-items: center; gap: 4px; }
  .fax-options i { width: 7px; height: 7px; background: var(--box-grey); display: inline-block; }
  .sheet-footer { position: absolute; left: 0; top: 423px; height: 27px; }
  .accent-bar { position: absolute; left: 0; top: 0; width: 4px; height: 26px; background: var(--accent); }
  .contact-list { position: absolute; left: 27px; top: 1px; font-size: 7px; line-height: 8.4px; color: var(--ink-soft); white-space: nowrap; list-style: none; }
  .contact-list li { display: flex; align-items: center; gap: 2px; }
  .contact-list svg { width: 6px; height: 6px; }

  /* Business cards */
  .card { width: 147px; height: 83px; border-radius: 6px; box-shadow: var(--shadow); overflow: hidden; }
  .card--front { left: 845px; top: 7px; background: var(--card-black); color: #fff; }
  .card--front .wordmark { left: 10px; top: 12px; font-size: 14px; }
  .card--front .accent-bar { top: 33px; height: 43px; }
  .card-name { position: absolute; left: 10px; top: 38px; font-size: 5px; line-height: 6px; }
  .card-name b { display: block; font-size: 5.4px; }
  .card-contacts { position: absolute; left: 10px; top: 52px; font-size: 3.6px; line-height: 5.6px; list-style: none; }
  .card-company { position: absolute; right: 8px; top: 62px; font-size: 3.6px; line-height: 4.6px; text-align: right; }
  .card-company b { font-size: 3.8px; }
  .card--back-white { left: 1010px; top: 7px; background: var(--paper); }
  .card--back-black { left: 920px; top: 103px; background: var(--card-black); color: #fff; }
  .card--back-white .wordmark, .card--back-black .wordmark { left: 0; right: 0; text-align: center; top: 22px; font-size: 20px; }
  .card-web { position: absolute; left: 0; right: 0; text-align: center; top: 64px; font-size: 5px; font-weight: 700; }
  .card--back-black .card-web { top: 63px; }

  /* Envelope */
  .flap { left: 794px; top: 199px; width: 397px; height: 46px; }
  .flap .wordmark { left: 0; right: 0; top: 14px; text-align: center; font-size: 12px; color: #fff; transform: rotate(180deg); }
  .envelope { left: 794px; top: 259px; width: 397px; height: 219px; box-shadow: var(--shadow); }
  .envelope > svg { position: absolute; inset: 0; }
  .envelope .flap-mark { left: 0; right: 0; top: 17px; text-align: center; font-size: 12px; transform: rotate(180deg); }
  .envelope .wordmark.return { left: 31px; top: 64px; font-size: 21px; }
  .return-address { position: absolute; left: 31px; top: 91px; width: 106px; text-align: center; font-size: 7.4px; line-height: 8.6px; color: var(--ink-soft); }
  .envelope .accent-bar { top: 193px; height: 14px; }
  .envelope-web { position: absolute; left: 25px; top: 195px; font-size: 5.6px; letter-spacing: 1.6px; font-weight: 700; color: #333; }
</style>
</head>
<body>

  <!-- Fax sheet -->
  <section class="sheet sheet--fax">
    <div class="wordmark">Brindle Works</div>
    <address class="sheet-address" style="font-style:normal">1475 Foundry Ln<br>Suite 310B<br>Ashford, VA 24190</address>
    <h1 class="fax-title">FAX</h1>
    <div class="fax-fields">
      <div class="fax-row"><span>To :</span><span>From :</span></div>
      <div class="fax-row"><span>Fax :</span><span>Page:</span></div>
      <div class="fax-row"><span>Phone :</span><span>Date:</span></div>
      <div class="fax-row"><span>Re :</span><span>CC:</span></div>
    </div>
    <div class="fax-options">
      <span><i></i>Urgent</span>
      <span><i></i>For Review</span>
      <span><i></i>Please Comment</span>
      <span><i></i>Please Reply</span>
      <span><i></i>Please Recycle</span>
    </div>
    <footer class="sheet-footer">
      <div class="accent-bar"></div>
      <ul class="contact-list">
        <li><svg viewBox="0 0 10 10"><path d="M2 1h2l1 3-1.5 1a6 6 0 0 0 2.5 2.5L7 6l3 1v2c-5 0-9-4-9-8z" fill="#666"/></svg>(000)000-0000</li>
        <li><svg viewBox="0 0 10 10"><rect x="1" y="4" width="8" height="5" fill="#666"/><rect x="3" y="1" width="4" height="3" fill="#666"/></svg>(000)000-0000</li>
        <li><svg viewBox="0 0 10 10"><circle cx="5" cy="5" r="4" fill="#666"/></svg>www.brindleworks.com</li>
      </ul>
    </footer>
  </section>

  <!-- Letterhead -->
  <section class="sheet sheet--letter">
    <div class="wordmark">Brindle Works</div>
    <address class="sheet-address" style="font-style:normal">1475 Foundry Ln<br>Suite 310B<br>Ashford, VA 24190</address>
    <footer class="sheet-footer">
      <div class="accent-bar"></div>
      <ul class="contact-list">
        <li><svg viewBox="0 0 10 10"><path d="M2 1h2l1 3-1.5 1a6 6 0 0 0 2.5 2.5L7 6l3 1v2c-5 0-9-4-9-8z" fill="#666"/></svg>(000)000-0000</li>
        <li><svg viewBox="0 0 10 10"><rect x="1" y="4" width="8" height="5" fill="#666"/><rect x="3" y="1" width="4" height="3" fill="#666"/></svg>(000)000-0000</li>
        <li><svg viewBox="0 0 10 10"><circle cx="5" cy="5" r="4" fill="#666"/></svg>www.brindleworks.com</li>
      </ul>
    </footer>
  </section>

  <!-- Business card front -->
  <section class="card card--front">
    <div class="wordmark">Brindle Works</div>
    <div class="accent-bar"></div>
    <div class="card-name"><b>Dana Whitlow</b>President</div>
    <ul class="card-contacts">
      <li>(000)000-00000</li>
      <li>(000)000-0000</li>
      <li>dana.whitlow@brindleworks.com</li>
      <li>www.brindleworks.com</li>
    </ul>
    <div class="card-company"><b>Brindle Works, LLC</b><br>1475 Foundry Ln, Suite 310B<br>Ashford, VA 24190</div>
  </section>

  <!-- Business card backs -->
  <section class="card card--back-white">
    <div class="wordmark">Brindle Works</div>
    <div class="card-web">www.brindleworks.com</div>
  </section>
  <section class="card card--back-black">
    <div class="wordmark">Brindle Works</div>
    <div class="card-web">www.brindleworks.com</div>
  </section>

  <!-- Envelope flap -->
  <section class="flap">
    <svg width="397" height="46" viewBox="0 0 397 46">
      <path d="M0 46 L30 6 Q34 0 42 0 L355 0 Q363 0 367 6 L397 46 Z" fill="var(--card-black)"/>
    </svg>
    <div class="wordmark">Brindle Works</div>
  </section>

  <!-- Envelope -->
  <section class="envelope">
    <svg width="397" height="219" viewBox="0 0 397 219">
      <path d="M0 219 V46 Q0 4 44 0 H353 Q397 4 397 46 V219 Z" fill="var(--paper)"/>
      <line x1="0" y1="46" x2="397" y2="46" stroke="#cfcfcf" stroke-width="1"/>
    </svg>
    <div class="wordmark flap-mark">Brindle Works</div>
    <div class="wordmark return">Brindle Works</div>
    <div class="return-address">1475 Foundry Ln, Suite 310B<br>Ashford, VA 24190</div>
    <div class="accent-bar"></div>
    <div class="envelope-web">www.brindleworks.com</div>
  </section>

</body>
</html>
```